Taking a stock layout (purchased) and making it consistent with our brand standards

Designers,

A friend of mine for a Catholic school district needs help with a poster.

The district consists of one high school and one elementary school. The poster design should be compatible for both schools. The schools have separate logos, but similar colors, so the poster designs should simply work for both (logos interchangeable, one logo on the design - NOT both).

My friend liked the following stock layout: http://www.plumfernprints.net/Files/PDF/Range/QM418-Range.pdf , so I purchased the attached native files.

So my project is to simply take the designs from the native files, and make a poster compatible with our brand colors/logo. I've attached PDFs of our current brochures (to use for colors) and the logos for both schools.

Reason: Have 2 great options, but I'm paying 3 spots so I'd like to get some more options

School

```html
<!DOCTYPE html>
<html lang="en">
<head>
<meta charset="utf-8">
<title>Larkhaven Catholic Central – Program Poster</title>
<link rel="stylesheet" href="https://fonts.googleapis.com/css2?family=Arimo:wght@400;700&family=Tinos&display=swap">
<style>
  :root {
    --page-bg: #e3e6e6;
    --white: #ffffff;
    --cyan: #72dcf5;
    --accent: #1f7bf0;
    --accent-mid: #4aa8f0;
    --bar: #fbbd3b;
    --heading: #2276e8;
    --contact: #2a72e0;
  }
  * { margin: 0; padding: 0; box-sizing: border-box; }
  html, body { width: 1200px; height: 1000px; overflow: hidden; background: var(--page-bg); }
  .stage { position: relative; width: 1200px; height: 1000px; }

  .poster {
    position: absolute; top: 143px; width: 510px; height: 722px;
    background: var(--white); overflow: hidden;
    font-family: "Arimo", Arial, sans-serif;
  }
  .poster--bright { left: 72px; }
  .poster--navy {
    left: 619px;
    --accent: #0c2a7e;
    --accent-mid: #3f8fe6;
    --bar: #b3b3b3;
    --heading: #0c2a7e;
    --contact: #0c2a7e;
  }

  .block { position: absolute; }
  .stripe-dark { left: 0; top: 0; width: 30px; height: 153px; background: var(--accent); }
  .stripe-light { left: 40px; top: 0; width: 18px; height: 153px; background: var(--accent-mid); }
  .photo-boy {
    left: 58px; top: 0; width: 132px; height: 153px;
    background: linear-gradient(90deg, var(--accent-mid) 0%, var(--accent) 45%, var(--bar) 60%, var(--accent-mid) 100%);
  }

  .mission-title {
    left: 260px; top: 0; width: 248px; height: 40px; background: var(--cyan);
    color: var(--white); font-size: 17px; font-weight: 400; letter-spacing: 0.6px;
    display: flex; align-items: center; justify-content: center;
  }
  .poster--navy .mission-title { background: var(--accent); }
  .mission-text {
    left: 260px; top: 40px; width: 248px; height: 72px; background: var(--accent);
    color: var(--white); font-size: 12px; line-height: 15px; text-align: center; padding-top: 5px;
  }

  .program-head {
    left: 260px; top: 120px; width: 248px; height: 32px; background: var(--bar);
    color: var(--white); font-size: 14px;
  }
  .program-head span { position: absolute; top: 8px; }
  .program-head .col-program { left: 52px; }
  .program-head .col-cost { left: 170px; }

  .program-panel { left: 260px; top: 156px; width: 248px; height: 420px; background: var(--cyan); }
  .program-row {
    position: absolute; left: 0; width: 248px; top: var(--y); height: var(--h);
    border-top: 1px solid var(--white); border-bottom: 1px solid var(--white);
    font-family: "Tinos", "Times New Roman", serif; font-size: 8px; line-height: 10.5px; color: var(--white);
  }
  .program-row .name { position: absolute; left: 6px; top: 3px; width: 132px; }
  .program-row .cost { position: absolute; left: 158px; top: 0; width: 90px; padding: 3px 4px 0 6px; border-left: 1px solid var(--white); height: 100%; }

  .about-panel { left: 0; top: 158px; width: 250px; height: 398px; background: var(--cyan); }
  .about-title {
    position: absolute; left: 22px; top: 21px; color: var(--heading);
    font-size: 22px; font-weight: 400; line-height: 28px;
  }
  .about-body {
    position: absolute; left: 22px; top: 93px; width: 225px; color: var(--white);
    font-family: "Tinos", "Times New Roman", serif; font-size: 13.2px; line-height: 16.4px;
  }
  .about-body p + p { margin-top: 16.4px; }
  .about-band { left: 0; top: 561px; width: 250px; height: 14px; background: var(--cyan); }

  .school-mark { left: 50px; top: 600px; width: 110px; display: flex; align-items: center; gap: 5px; }
  .school-mark .dot { width: 16px; height: 16px; border-radius: 50%; background: var(--accent); flex: none; }
  .school-mark .name { color: var(--contact); font-size: 11px; line-height: 13px; font-weight: 700; }

  .contact {
    left: 160px; top: 601px; width: 180px; text-align: center; font-style: normal;
    color: var(--contact); font-size: 11px; line-height: 14.4px;
  }
  .poster--navy .contact { top: 594px; line-height: 13.6px; }

  .photo-girl {
    left: 332px; top: 545px; width: 176px; height: 177px;
    background: linear-gradient(160deg, var(--accent) 0%, var(--accent-mid) 55%, var(--cyan) 100%);
  }
  .color-band {
    left: 0; top: 690px; width: 332px; height: 32px;
    background: linear-gradient(90deg, var(--accent-mid) 0%, var(--cyan) 35%, var(--bar) 60%, var(--accent-mid) 100%);
  }
</style>
</head>
<body>
<main class="stage">

  <article class="poster poster--bright">
    <div class="block stripe-dark"></div>
    <div class="block stripe-light"></div>
    <div class="block photo-boy" role="img" aria-label="Portrait of a smiling boy in blue and yellow duotone"></div>

    <h2 class="block mission-title">Mission Statemen</h2>
    <p class="block mission-text">We are Larkhaven,<br>called by Christ to<br>learn, love and lead...<br>courageously</p>

    <div class="block program-head"><span class="col-program">Program</span><span class="col-cost">Cost</span></div>
    <div class="block program-panel">
      <div class="program-row" style="--y:3px;--h:39px"><div class="name">Traditional – 3 years old – Tuesdays and Thursdays&nbsp; Half Day: 8am-11am</div><div class="cost">$800 a year</div></div>
      <div class="program-row" style="--y:42px;--h:30px"><div class="name">Traditional – 3 years old – Tuesdays and Thursdays&nbsp; Full Day: 8am-3pm</div><div class="cost">$1700 a year</div></div>
      <div class="program-row" style="--y:77px;--h:40px"><div class="name">Traditional – 4 years old – Mondays, Wednesdays, Fridays Half Day: 8am-11am</div><div class="cost">$950 a year</div></div>
      <div class="program-row" style="--y:117px;--h:41px"><div class="name">Traditional – 4 years old – Mondays, Wednesdays, Fridays&nbsp; Full Day: 8am-3pm</div><div class="cost">$2550 a year</div></div>
      <div class="program-row" style="--y:164px;--h:24px"><div class="name">Montessori – 3 years old – Three ½</div><div class="cost">$950 a&nbsp; year</div></div>
      <div class="program-row" style="--y:188px;--h:24px"><div class="name">Montessori – 3 years old – Three full</div><div class="cost">$2550 a year</div></div>
      <div class="program-row" style="--y:218px;--h:42px"><div class="name">Montessori – 3, 4, or 5 years old – Mondays through Fridays&nbsp; Half Day: 8am-11am</div><div class="cost">$2500 a year</div></div>
      <div class="program-row" style="--y:260px;--h:44px"><div class="name">Montessori – 3, 4, or 5 years old – Mondays through Fridays&nbsp; Full Day: 8am-3pm</div><div class="cost">$4250 a year</div></div>
      <div class="program-row" style="--y:309px;--h:43px"><div class="name">Young Fives – 5 years old – Mondays through Fridays&nbsp; Half Day: 8am-11am</div><div class="cost">$2550 or&nbsp; 6% of Adjusted Gross Income</div></div>
      <div class="program-row" style="--y:352px;--h:44px"><div class="name">Young Fives – 5 years old – Mondays through Fridays&nbsp; Full Day: 8am-3pm</div><div class="cost">$4250 or 6% of Adjusted Gross Income</div></div>
    </div>

    <section class="block about-panel">
      <h1 class="about-title">Catholic<br>Education</h1>
      <div class="about-body">
        <p>Catholic education has a strong,<br>rich history in Birchmont County.<br>Our mission of educating students<br>to excel academically in a faith-based<br>enviroment dates back to 1878.<br>Many things may have changed<br>since 1878, but some things hold<br>true yet today. We continue to<br>provide an outstanding academic<br>education in a Christ-centered<br>learning enviroment and we continue<br>to shape future leaders of our church<br>and our world.</p>
        <p>We invite you to see for yourself<br>the Larkhaven Difference. Call today<br>to set up your personal tour.</p>
      </div>
    </section>
    <div class="block about-band"></div>

    <div class="block school-mark"><span class="dot"></span><span class="name">Larkhaven Catholic Central</span></div>
    <address class="block contact">418 Quarry Lane<br>Birchmont MI 48120<br>(555) 014-2361<br>office@larkhavenschools.org<br>www.larkhavenschools.org</address>

    <div class="block color-band" role="img" aria-label="Decorative band of coloured vertical bars"></div>
    <div class="block photo-girl" role="img" aria-label="Portrait of a smiling girl in blue duotone"></div>
  </article>

  <article class="poster poster--navy">
    <div class="block stripe-dark"></div>
    <div class="block stripe-light"></div>
    <div class="block photo-boy" role="img" aria-label="Portrait of a smiling boy in navy and grey duotone"></div>

    <h2 class="block mission-title">Mission Statemen</h2>
    <p class="block mission-text">We are Larkhaven,<br>called by Christ to<br>learn, love and lead...<br>courageously</p>

    <div class="block program-head"><span class="col-program">Program</span><span class="col-cost">Cost</span></div>
    <div class="block program-panel">
      <div class="program-row" style="--y:3px;--h:39px"><div class="name">Traditional – 3 years old – Tuesdays and Thursdays&nbsp; Half Day: 8am-11am</div><div class="cost">$800 a year</div></div>
      <div class="program-row" style="--y:42px;--h:30px"><div class="name">Traditional – 3 years old – Tuesdays and Thursdays&nbsp; Full Day: 8am-3pm</div><div class="cost">$1700 a year</div></div>
      <div class="program-row" style="--y:77px;--h:40px"><div class="name">Traditional – 4 years old – Mondays, Wednesdays, Fridays Half Day: 8am-11am</div><div class="cost">$950 a year</div></div>
      <div class="program-row" style="--y:117px;--h:41px"><div class="name">Traditional – 4 years old – Mondays, Wednesdays, Fridays&nbsp; Full Day: 8am-3pm</div><div class="cost">$2550 a year</div></div>
      <div class="program-row" style="--y:164px;--h:24px"><div class="name">Montessori – 3 years old – Three ½</div><div class="cost">$950 a&nbsp; year</div></div>
      <div class="program-row" style="--y:188px;--h:24px"><div class="name">Montessori – 3 years old – Three full</div><div class="cost">$2550 a year</div></div>
      <div class="program-row" style="--y:218px;--h:42px"><div class="name">Montessori – 3, 4, or 5 years old – Mondays through Fridays&nbsp; Half Day: 8am-11am</div><div class="cost">$2500 a year</div></div>
      <div class="program-row" style="--y:260px;--h:44px"><div class="name">Montessori – 3, 4, or 5 years old – Mondays through Fridays&nbsp; Full Day: 8am-3pm</div><div class="cost">$4250 a year</div></div>
      <div class="program-row" style="--y:309px;--h:43px"><div class="name">Young Fives – 5 years old – Mondays through Fridays&nbsp; Half Day: 8am-11am</div><div class="cost">$2550 or&nbsp; 6% of Adjusted Gross Income</div></div>
      <div class="program-row" style="--y:352px;--h:44px"><div class="name">Young Fives – 5 years old – Mondays through Fridays&nbsp; Full Day: 8am-3pm</div><div class="cost">$4250 or 6% of Adjusted Gross Income</div></div>
    </div>

    <section class="block about-panel">
      <h1 class="about-title">Catholic<br>Education</h1>
      <div class="about-body">
        <p>Catholic education has a strong,<br>rich history in Birchmont County.<br>Our mission of educating students<br>to excel academically in a faith-based<br>enviroment dates back to 1878.<br>Many things may have changed<br>since 1878, but some things hold<br>true yet today. We continue to<br>provide an outstanding academic<br>education in a Christ-centered<br>learning enviroment and we continue<br>to shape future leaders of our church<br>and our world.</p>
        <p>We invite you to see for yourself<br>the Larkhaven Difference. Call today<br>to set up your personal tour.</p>
      </div>
    </section>
    <div class="block about-band"></div>

    <div class="block school-mark"><span class="dot"></span><span class="name">Larkhaven Catholic Central</span></div>
    <address class="block contact">Larkhaven Catholic Central<br>High School<br>(555) 014-4330<br>Larkhaven Catholic Central<br>Lementary School<br>(555) 014-2361</address>

    <div class="block color-band" role="img" aria-label="Decorative band of coloured vertical bars"></div>
    <div class="block photo-girl" role="img" aria-label="Portrait of a smiling girl in navy duotone"></div>
  </article>

</main>
</body>
</html>
```